Adventurous female pilot

I am looking for a personal business card, for a very well qualified female pilot, with a lot of aviation experience.

Currently an airline pilot, have worked as a bush pilot in Africa, looking to get into corporate aviation, or private jet owners.
Want a classy looking card for networking...

Could be interested in a retro\vintage look also?!

An idea,, is an african sunset background, with my wings\logo on it
Updates

I just want to say thank you to all of your for your amazing designs!

I have been very busy flying this past week , so not had a chance to be on the computer much.
But I provide some feedback, and conclusions very soon!
Thank you again.

Marla

Reason: Still waiting on a couple of revisions to be 100% about my choice!

Target Market(s)

corporate aviation, private jet owners, casino's,
General audience.
networking

Industry/Entity Type

Airline

Requirements
Nice to have
• Classy, edgy, sexy, but also feminine

```html
<!DOCTYPE html>
<html lang="en">
<head>
<meta charset="utf-8">
<title>Marla Prince – Business Card</title>
<link rel="stylesheet" href="https://fonts.googleapis.com/css2?family=Open+Sans:wght@300;400;600&display=swap">
<style>
  :root {
    --backdrop: #e9e4da;
    --card-light: #f3ee8a;
    --card-mid: #e9e04a;
    --card-deep: #dccd2a;
    --swirl-light: #f6c21a;
    --swirl-deep: #ef9a16;
    --name-pink: #ef8a86;
    --ink: #6b5a2a;
    --ink-soft: #8a7a3c;
  }
  * { margin: 0; padding: 0; box-sizing: border-box; }
  html, body {
    width: 1200px; height: 801px; overflow: hidden;
    background: var(--backdrop);
    font-family: "Open Sans", sans-serif;
  }
  .stage {
    width: 1200px; height: 801px;
    display: flex; align-items: center; justify-content: center;
  }
  .business-card {
    position: relative;
    width: 980px; height: 580px;
    background: linear-gradient(115deg, var(--card-light) 0%, var(--card-mid) 55%, var(--card-deep) 100%);
    box-shadow: 0 18px 40px rgba(80, 60, 20, 0.25);
    overflow: hidden;
  }
  .ornament {
    position: absolute;
    right: 40px; top: 36px;
    width: 420px; height: 190px;
  }
  .identity {
    position: absolute;
    left: 80px; top: 120px;
    display: flex; align-items: center; gap: 14px;
  }
  .identity-mark {
    width: 22px; height: 22px; border-radius: 50%;
    background: var(--ink);
  }
  .identity-name {
    font-size: 22px; font-weight: 400; letter-spacing: 2px;
    color: var(--ink); text-transform: uppercase;
  }
  .identity-role {
    position: absolute;
    left: 116px; top: 156px;
    font-size: 12px; letter-spacing: 3px;
    color: var(--ink-soft); text-transform: uppercase;
  }
  .holder-name {
    position: absolute;
    left: 80px; top: 252px;
    font-size: 58px; font-weight: 300; line-height: 1.2;
    color: var(--name-pink);
    white-space: nowrap;
  }
  .contact {
    position: absolute;
    left: 80px; top: 360px;
    display: flex; flex-direction: column; gap: 26px;
  }
  .contact-row {
    display: flex; align-items: flex-start; gap: 18px;
    font-size: 22px; font-weight: 300; color: var(--ink-soft);
    line-height: 1.35;
  }
  .contact-icon { width: 26px; height: 26px; flex: none; margin-top: 3px; }
</style>
</head>
<body>
<main class="stage">
  <section class="business-card">
    <svg class="ornament" viewBox="0 0 420 190" role="img" aria-label="Flowing golden-orange flourish ornament">
      <defs>
        <linearGradient id="flourishTone" x1="0" y1="0" x2="1" y2="1">
          <stop offset="0" stop-color="var(--swirl-light)" stop-opacity="0.85"/>
          <stop offset="1" stop-color="var(--swirl-deep)" stop-opacity="0.85"/>
        </linearGradient>
      </defs>
      <rect x="0" y="0" width="420" height="190" rx="95" fill="url(#flourishTone)" opacity="0.55"/>
    </svg>

    <div class="identity">
      <span class="identity-mark"></span>
      <span class="identity-name">Marla Prince</span>
    </div>
    <div class="identity-role">Aviator</div>

    <h1 class="holder-name">Marla Prince</h1>

    <div class="contact">
      <div class="contact-row">
        <svg class="contact-icon" viewBox="0 0 24 24" aria-hidden="true">
          <path d="M6.6 10.8a15 15 0 0 0 6.6 6.6l2.2-2.2a1 1 0 0 1 1-.25 11.4 11.4 0 0 0 3.6.57 1 1 0 0 1 1 1V20a1 1 0 0 1-1 1A17 17 0 0 1 3 4a1 1 0 0 1 1-1h3.5a1 1 0 0 1 1 1c0 1.25.2 2.45.57 3.6a1 1 0 0 1-.25 1z" fill="var(--name-pink)"/>
        </svg>
        <div>+1 702 555 0143<br>+886 970 555 214</div>
      </div>
      <div class="contact-row">
        <svg class="contact-icon" viewBox="0 0 24 24" aria-hidden="true">
          <rect x="2" y="5" width="20" height="14" rx="2" fill="var(--name-pink)"/>
          <path d="M3 6l9 7 9-7" fill="none" stroke="var(--card-light)" stroke-width="1.5"/>
        </svg>
        <div>marlaprince@skymail.com</div>
      </div>
    </div>
  </section>
</main>
</body>
</html>
```